Biz Card for Harrowfield Property Partners - HWPP

Harrowfield Property Partners is a commercial real estate acquisitions firm. We buy commercial property and need to raise capital from investors for each deal we buy. The vibe needs to be: give us your money, we will multiply it.
Our website: www.hrwpp-example.com
Competitors are: https://velmarholdings-example.com/, https://tribanquepartners-example.com/, http://www.ostrellecapital-example.com/
Target Market(s)
High Net Worth Individuals, Bankers, Insurance Companies, Commercial Real Estate Brokers.
Industry/Entity Type
Investment Banking
Contact Information for Business Card
Name, Title, Addess, Cell#, Office#, email, website
Requirements
Must have
- use one of our logos. See website for look and feel: www.hrwpp-example.com
Nice to have
- see website: www.hrwpp-example.com

```html
<!DOCTYPE html>
<html lang="en">
<head>
<meta charset="utf-8">
<title>Harrowfield Property Partners – Business Card</title>
<link href="https://fonts.googleapis.com/css2?family=Montserrat:wght@400;500&family=Work+Sans:wght@400;600&display=swap" rel="stylesheet">
<style>
  :root {
    --navy: #0f2a44;
    --navy-deep: #08203a;
    --ink: #1c2b3a;
    --grey: #4a5560;
    --paper: #ffffff;
    --backdrop: #1b1b1c;
  }
  * { box-sizing: border-box; margin: 0; padding: 0; }
  html, body { width: 1200px; height: 930px; overflow: hidden; }
  body { background: var(--backdrop); position: relative; font-family: "Work Sans", Arial, sans-serif; }

  .card {
    position: absolute;
    width: 600px; height: 343px;
    border-radius: 22px;
    overflow: hidden;
    box-shadow: 0 18px 40px rgba(0,0,0,.55);
  }

  /* Back of card */
  .card-back {
    left: 110px; top: 80px;
    background: linear-gradient(135deg, #1a3a5a 0%, var(--navy) 45%, var(--navy-deep) 100%);
    color: var(--paper);
  }
  .card-back .brand-mark {
    position: absolute; left: 50%; top: 58px;
    width: 104px; height: 104px; margin-left: -52px;
    border-radius: 50%; background: var(--paper);
  }
  .card-back .brand-name {
    position: absolute; left: 0; right: 0; top: 186px;
    text-align: center;
    font-family: "Montserrat", Arial, sans-serif; font-weight: 400;
    color: var(--paper);
  }
  .brand-name .line-main { display: block; font-size: 42px; letter-spacing: 10px; line-height: 1; }
  .brand-name .line-sub { display: block; font-size: 14px; letter-spacing: 6px; margin-top: 10px; }

  /* Front of card */
  .card-front { left: 490px; top: 500px; background: var(--paper); }
  .card-front .brand-name {
    position: absolute; left: 44px; top: 50px;
    font-family: "Montserrat", Arial, sans-serif; font-weight: 400;
    color: var(--navy);
  }
  .card-front .brand-name .line-main { font-size: 25px; letter-spacing: 6px; }
  .card-front .brand-name .line-sub { font-size: 9px; letter-spacing: 3.5px; margin-top: 6px; }

  .side-tab {
    position: absolute; left: 0; top: 156px;
    width: 10px; height: 34px; background: var(--navy);
  }
  .person { position: absolute; left: 44px; top: 148px; }
  .person-name { font-weight: 600; font-size: 17px; color: var(--navy); letter-spacing: .5px; }
  .person-title { font-size: 14px; color: var(--grey); margin-top: 2px; }
  .address { font-size: 14px; color: var(--grey); line-height: 1.3; margin-top: 10px; font-style: normal; }
  .contact { list-style: none; margin-top: 10px; font-size: 14px; color: var(--grey); }
  .contact li { display: flex; align-items: center; gap: 8px; line-height: 1.45; }
  .contact svg { width: 11px; height: 11px; flex: none; }
  .contact strong { color: var(--navy); font-weight: 600; }

  .brand-disc {
    position: absolute; right: 40px; top: 28px;
    width: 300px; height: 300px; border-radius: 50%;
    background: linear-gradient(135deg, #1c3d5e 0%, var(--navy) 50%, var(--navy-deep) 100%);
  }
</style>
</head>
<body>

  <section class="card card-back">
    <div class="brand-mark" aria-hidden="true"></div>
    <div class="brand-name">
      <span class="line-main">HARROWFIELD</span>
      <span class="line-sub">PROPERTY PARTNERS</span>
    </div>
  </section>

  <section class="card card-front">
    <div class="brand-name">
      <span class="line-main">HARROWFIELD</span>
      <span class="line-sub">PROPERTY PARTNERS</span>
    </div>

    <div class="side-tab" aria-hidden="true"></div>

    <div class="person">
      <p class="person-name">DORIAN KELLER</p>
      <p class="person-title">Founder</p>
      <address class="address">418 Marlow Ave,<br>Suite 910 Westbrook,<br>FL 33201</address>
      <ul class="contact">
        <li>
          <svg viewBox="0 0 12 12"><path d="M2.5 1 L4.5 1 L5.2 3.6 L3.9 4.6 Q5 7 7.4 8.1 L8.4 6.8 L11 7.5 L11 9.5 Q11 11 9.5 11 Q1 10 1 2.5 Q1 1 2.5 1 Z" fill="#0f2a44"/></svg>
          (555) 014-2290
        </li>
        <li>
          <svg viewBox="0 0 12 12"><rect x="1" y="2.5" width="10" height="7" fill="none" stroke="#0f2a44" stroke-width="1.2"/><path d="M1 2.5 L6 6.5 L11 2.5" fill="none" stroke="#0f2a44" stroke-width="1.2"/></svg>
          info@hrwpp-example.com
        </li>
        <li>
          <svg viewBox="0 0 12 12"><circle cx="6" cy="6" r="5" fill="none" stroke="#0f2a44" stroke-width="1.1"/><ellipse cx="6" cy="6" rx="2.2" ry="5" fill="none" stroke="#0f2a44" stroke-width="1"/><path d="M1 6 H11" stroke="#0f2a44" stroke-width="1"/></svg>
          <span>www.<strong>hrwpp-example</strong>.com</span>
        </li>
      </ul>
    </div>

    <div class="brand-disc" aria-hidden="true"></div>
  </section>

</body>
</html>
```